Financial Advisor / Asset Manager Zup Design

I'm currently hosting with Zup and my first attempt at a website is live at www.ravenholtwealth.example Clearly I am not a web designer and I need help making this more catchy, modern, cross-platform compatible, search engine optimized, etc. I've got logos, hex color pallets, and a slew of other graphics. I'm interested in working with a winning designer to write/refine my copy/language to complete the build.

Full set of graphics https://pics.lumora-share.example/q71TzR05KwPd2MhXN do NOT use the CONSULTING graphics as this is for a related business / different website

Target Market(s)

Individuals, small institutions, endowments, non-profits seeking financial advice and asset / portfolio management

Industry/Entity Type

Financial Services

Coding

Coded - Design and coding required

Font styles to use
Other font styles liked:
• AvenirLTStd - Black, Book, and Roman as appropriate

Requirements
Must have
• Complete, cross platform website integrating my existing logo
Nice to have
• Easy to update format for go-forward maintenance

```html
<!DOCTYPE html>
<html lang="en">
<head>
<meta charset="utf-8">
<title>Ravenholt Wealth – Personalized Financial Advice</title>
<link href="https://fonts.googleapis.com/css2?family=Montserrat:wght@300;400;600;700&family=Nunito+Sans:wght@400;600;700;800;900&display=swap" rel="stylesheet">
<style>
:root{
  --sky:#13a3e8;
  --blue:#0f7fd1;
  --deep:#0b63b8;
  --navy:#0a4f9e;
  --ink:#1b1b1b;
  --text:#444;
  --muted:#666;
  --line:#d6d6d6;
  --white:#fff;
}
*{box-sizing:border-box;margin:0;padding:0}
html,body{width:1200px;height:4762px;overflow:hidden}
body{position:relative;font-family:"Nunito Sans",sans-serif;color:var(--text);background:var(--white)}
.abs{position:absolute}
.heading{font-family:"Montserrat",sans-serif;font-weight:300;color:var(--ink);letter-spacing:.5px}
.underline{display:block;width:74px;height:2px;background:var(--sky);margin:10px auto 0}
.btn{display:flex;align-items:center;justify-content:center;background:var(--blue);color:var(--white);font-weight:800;font-size:14px;letter-spacing:.4px;border-radius:3px}
.brand{display:flex;align-items:center;gap:10px;color:var(--white);font-family:"Montserrat",sans-serif;font-weight:400;font-size:21px;letter-spacing:1px}
.brand-mark{width:14px;height:14px;border-radius:50%;background:var(--white)}

/* header + hero */
.hero{left:0;top:0;width:1200px;height:719px;background:linear-gradient(180deg,#3f8fd6 0%,#9cc6ea 35%,#e3eef8 62%,#8da1b8 80%,#dfe6ee 100%)}
.site-header{left:0;top:0;width:1200px;height:63px;background:rgba(14,110,200,.55)}
.site-header .brand{position:absolute;left:100px;top:16px}
.nav{position:absolute;right:100px;top:0;height:63px;display:flex;align-items:center;gap:28px;color:var(--white);font-family:"Montserrat",sans-serif;font-weight:600;font-size:13px}
.nav .sep{opacity:.8}
.nav .active{position:relative}
.nav .active::after{content:"";position:absolute;left:0;right:0;bottom:-20px;height:2px;background:var(--white)}
.hero-title{left:0;top:175px;width:1200px;text-align:center;font-family:"Montserrat",sans-serif;font-weight:300;font-size:38px;line-height:45px;color:var(--white)}
.hero .btn{left:524px;top:285px;width:152px;height:42px}
.dots{left:552px;top:674px;display:flex;gap:16px}
.dots span{width:12px;height:12px;border:1.5px solid var(--white);border-radius:50%}
.dots .on{background:var(--white)}

/* values band */
.values{left:0;top:719px;width:1200px;height:307px;display:flex}
.value{width:300px;height:307px;color:var(--white);text-align:center;padding-top:60px}
.value:nth-child(1){background:var(--sky)}
.value:nth-child(2){background:var(--deep)}
.value:nth-child(3){background:#1a9de3}
.value:nth-child(4){background:#0c5cb2}
.value svg{width:84px;height:84px}
.value h3{font-weight:800;font-size:24px;margin:26px 0 12px}
.value p{font-size:15px;line-height:25px;width:240px;margin:0 auto}

/* who we are */
.who{left:0;top:1026px;width:1200px;height:592px;background:var(--white)}
.who-panel{left:826px;top:0;width:374px;height:592px;background:linear-gradient(160deg,#1a97e0,#0b5fb4 70%,#0a56a8)}
.who .heading{left:100px;top:124px;font-size:46px}
.who-copy{left:100px;top:198px;width:450px;font-size:14.5px;line-height:32px;text-align:justify;color:var(--text)}
.who .btn{left:100px;top:414px;width:152px;height:44px}
.portrait{left:613px;top:98px;width:487px;height:397px;background:linear-gradient(135deg,#8b7a4a,#b39a66 40%,#5c6f3e 75%,#3d4b2c)}

/* offer */
.offer{left:0;top:1618px;width:1200px;height:1156px;background:linear-gradient(180deg,#0c60b4 0%,#1a72c4 50%,#2c6fae 80%,#0c5eb0 100%)}
.offer .heading{left:0;top:94px;width:1200px;text-align:center;font-size:46px;color:var(--white)}
.offer .underline{background:var(--white)}
.cards{left:100px;top:176px;width:1000px;display:grid;grid-template-columns:repeat(3,316px);column-gap:26px;row-gap:26px}
.card{position:relative;height:425px;background:var(--white);border-radius:3px;text-align:center}
.card-photo{height:214px;border-radius:3px 3px 0 0}
.card-icon{position:absolute;left:118px;top:174px;width:80px;height:80px;border-radius:50%;background:var(--blue);border:4px solid var(--white);display:flex;align-items:center;justify-content:center}
.card h4{margin-top:68px;font-family:"Montserrat",sans-serif;font-weight:700;font-size:19px;color:var(--ink)}
.card p{width:270px;margin:12px auto 0;font-size:13px;line-height:21px;color:var(--text)}
.card a{display:inline-block;margin-top:12px;font-weight:800;font-size:14px;color:var(--deep);text-decoration:underline}

/* faq */
.faq{left:0;top:2774px;width:1200px;height:739px}
.faq .heading{left:0;top:92px;width:1200px;text-align:center;font-size:40px}
.faq-list{left:155px;top:186px;width:890px}
.faq-item{height:62px;margin-bottom:26px;background:var(--white);box-shadow:0 1px 6px rgba(0,0,0,.18);display:flex;align-items:center;justify-content:space-between;padding-left:26px;font-size:20px;color:#333}
.faq-plus{width:58px;height:50px;margin-right:6px;background:var(--deep);display:flex;align-items:center;justify-content:center}

/* contact */
.contact{left:0;top:3513px;width:1200px;height:814px;background:linear-gradient(180deg,#fff 0%,#fff 52%,#d9e3ee 60%,#b9835a 72%,#d47a3d 80%,#8a5a3e 88%,#2e3a2a 100%)}
.contact h2{position:absolute;left:0;top:60px;width:1200px;text-align:center;font-family:"Montserrat",sans-serif;font-weight:700;font-size:36px;color:var(--ink)}
.contact .lead{left:290px;top:116px;width:620px;text-align:center;font-size:15px;line-height:26px;color:var(--text)}
.info{left:160px;top:230px;color:var(--ink)}
.info h5{font-family:"Montserrat",sans-serif;font-weight:700;font-size:17px;margin-bottom:8px}
.info p{font-size:15px;line-height:22px;color:var(--text);margin-bottom:28px}
.socials{display:flex;gap:12px}
.socials span{width:40px;height:40px;border-radius:50%;background:var(--deep);border:2px solid var(--white)}
.form{left:509px;top:194px;width:531px;height:398px;background:var(--white);box-shadow:0 2px 10px rgba(0,0,0,.12);padding:30px 40px}
.form h5{font-family:"Montserrat",sans-serif;font-weight:700;font-size:17px;color:var(--ink);margin-bottom:30px}
.field{display:flex;justify-content:space-between;align-items:center;border-bottom:1px solid var(--line);height:44px;margin-bottom:28px;font-size:15px;color:#555}
.field.tall{height:70px;align-items:flex-start}
.form .btn{position:absolute;right:40px;bottom:34px;width:242px;height:46px}

/* footer */
.footer{left:0;top:4327px;width:1200px;height:435px;background:var(--deep);color:var(--white)}
.footer .brand{position:absolute;left:100px;top:92px}
.footer .socials{position:absolute;left:118px;top:166px;gap:14px}
.footer .socials span{width:40px;height:40px;background:transparent;border:1.5px solid var(--white)}
.vrule{position:absolute;top:90px;width:2px;height:170px;background:rgba(255,255,255,.35)}
.vrule::before{content:"";position:absolute;left:0;top:0;width:2px;height:30px;background:var(--white)}
.fcol{position:absolute;top:86px;font-size:14px}
.fcol h6{font-weight:800;font-size:16px;margin-bottom:16px}
.fcol li{list-style:none;margin-bottom:14px}
.fcol .row{display:flex;gap:8px;margin-bottom:16px;line-height:20px}
.copyright{position:absolute;left:100px;top:386px;font-size:13px}
.legal{position:absolute;right:100px;top:386px;font-size:13px}
</style>
</head>
<body>

<section class="abs hero">
  <div class="abs" role="img" aria-label="Snow-capped mountain range above a layer of clouds over a winter field" style="left:0;top:230px;width:1200px;height:420px;background:linear-gradient(180deg,rgba(255,255,255,0) 0%,rgba(90,110,135,.55) 35%,rgba(240,244,248,.9) 60%,rgba(60,70,80,.35) 78%,rgba(225,232,240,1) 100%)"></div>
  <header class="abs site-header">
    <div class="brand"><span class="brand-mark"></span>RAVENHOLT WEALTH</div>
    <nav class="nav">
      <span class="active">HOME</span><span class="sep">|</span>
      <span>ABOUT</span><span class="sep">|</span>
      <span>FAQS</span><span class="sep">|</span>
      <span>SERVICES ▾</span><span class="sep">|</span>
      <span>CONTACT</span>
    </nav>
  </header>
  <h1 class="abs hero-title">PERSONALIZED FINANCIAL&nbsp; ADVICE TO<br>HELP YOU ACHIEVE YOUR GOALS</h1>
  <div class="abs btn">GET STARTED</div>
  <div class="abs dots"><span></span><span class="on"></span><span></span><span></span></div>
</section>

<section class="abs values">
  <div class="value">
    <svg viewBox="0 0 84 84" fill="none" stroke="#fff" stroke-width="2.5"><circle cx="28" cy="22" r="7"/><circle cx="42" cy="18" r="7"/><circle cx="56" cy="22" r="7"/><path d="M16 44c2-8 8-12 12-12M42 28c8 0 14 6 14 14M68 44c-2-8-8-12-12-12"/><path d="M10 58h14l12 6h22l16-10M10 70h16l14 6h30"/></svg>
    <h3>You Come First</h3><p>We always act in the best interests of our clients</p>
  </div>
  <div class="value">
    <svg viewBox="0 0 84 84" fill="none" stroke="#fff" stroke-width="2.5"><circle cx="42" cy="42" r="26"/><circle cx="42" cy="42" r="16"/><path d="M42 8v8M42 68v8M8 42h8M68 42h8M18 18l6 6M60 60l6 6M66 18l-6 6M24 60l-6 6"/><circle cx="42" cy="38" r="5"/><path d="M33 51c2-5 5-7 9-7s7 2 9 7"/></svg>
    <h3>Personalized Services</h3><p>We get to know you in order to service your unique needs</p>
  </div>
  <div class="value">
    <svg viewBox="0 0 84 84" fill="none" stroke="#fff" stroke-width="2.5"><circle cx="46" cy="22" r="14"/><path d="M50 16h-6a3 3 0 000 6h4a3 3 0 010 6h-6M46 12v4M46 28v4"/><path d="M10 56l14-8h16l6 4H32M46 52l18-10 6 4-24 18H22l-12 6"/></svg>
    <h3>Transparent Fees</h3><p>You'll always know what you pay and how we get paid</p>
  </div>
  <div class="value">
    <svg viewBox="0 0 84 84" fill="none" stroke="#fff" stroke-width="2.5"><path d="M52 34c-6-6-14 0-8 8l8 8 8-8c6-8-2-14-8-8z"/><path d="M14 52l14-8h16l6 4H34M50 48l18-10 6 4-24 18H26l-12 6"/><path d="M30 26l10-14 10 8"/></svg>
    <h3>We Give Back</h3><p>We support and better our local communities</p>
  </div>
</section>

<section class="abs who">
  <div class="abs who-panel" role="img" aria-label="Soft blue mountain backdrop"></div>
  <h2 class="abs heading">WHO WE ARE</h2>
  <p class="abs who-copy">Ravenholt Wealth is a registered investment advisory firm committed to serving as fiduciary to our clients. We always act in the best interests of our clients, including putting your interests ahead of our own. We provide independent financial planning, investment management, and asset management services tailored to your unique needs &amp; circumstances.</p>
  <div class="abs btn">LEARN MORE</div>
  <div class="abs portrait" role="img" aria-label="Portrait photo of the firm's advisor outdoors with autumn trees behind"></div>
</section>

<section class="abs offer">
  <h2 class="abs heading">WHAT WE OFFER<span class="underline"></span></h2>
  <div class="abs cards">
    <article class="card">
      <div class="card-photo" role="img" aria-label="Hands at a laptop with market charts" style="background:linear-gradient(135deg,#3a4a66,#c0504d 60%,#2b3f5e)"></div>
      <div class="card-icon"><svg width="40" height="40" viewBox="0 0 40 40" fill="none" stroke="#fff" stroke-width="2"><path d="M6 34h28M10 30V20M16 30V16M22 30V22M28 30V12"/></svg></div>
      <h4>STOCK SELECTION</h4>
      <p>You and your circumstances are unique. We want to know you where you are today, and help you get</p>
      <a>LEARN MORE</a>
    </article>
    <article class="card">
      <div class="card-photo" role="img" aria-label="Businessman with glowing digital growth charts" style="background:linear-gradient(135deg,#7cc8ec,#1e5c9a 55%,#0d2c55)"></div>
      <div class="card-icon"><svg width="40" height="40" viewBox="0 0 40 40" fill="none" stroke="#fff" stroke-width="2"><circle cx="14" cy="12" r="4"/><circle cx="26" cy="12" r="4"/><circle cx="20" cy="26" r="4"/><path d="M12 36c0-4 4-6 8-6s8 2 8 6"/></svg></div>
      <h4>ALTERNATIVES</h4>
      <p>The challenges facing investors seeking to build portfolios capable of generating attractive returns with acceptable</p>
      <a>LEARN MORE</a>
    </article>
    <article class="card">
      <div class="card-photo" role="img" aria-label="Two colleagues reviewing a chart on a whiteboard" style="background:linear-gradient(135deg,#5d7186,#d9e1e8 60%,#b7c4cf)"></div>
      <div class="card-icon"><svg width="40" height="40" viewBox="0 0 40 40" fill="none" stroke="#fff" stroke-width="2"><rect x="6" y="8" width="28" height="22"/><path d="M10 26l6-6 5 4 9-10"/></svg></div>
      <h4>OPTIMIZATION</h4>
      <p>You and your circumstances are unique. We Your investment portfolio was built with money you earned.</p>
      <a>LEARN MORE</a>
    </article>
    <article class="card">
      <div class="card-photo" role="img" aria-label="Calculator, coins and pen on financial papers" style="background:linear-gradient(135deg,#8a7a5c,#d8d2c4 55%,#9aa3ad)"></div>
      <div class="card-icon"><svg width="40" height="40" viewBox="0 0 40 40" fill="none" stroke="#fff" stroke-width="2"><rect x="10" y="6" width="20" height="28"/><path d="M14 12h12M14 18h4M22 18h4M14 24h4M22 24h4M14 30h12"/></svg></div>
      <h4>FINANCIAL PLANNING</h4>
      <p>Sed ut perspiciatis unde omnis iste natus error sit voluptatem accusanti doloremque laudantium, totam rem aperiam</p>
      <a>LEARN MORE</a>
    </article>
    <article class="card">
      <div class="card-photo" role="img" aria-label="Hand with pen analyzing printed charts" style="background:linear-gradient(135deg,#6b6f75,#e0e2e5 55%,#8b9097)"></div>
      <div class="card-icon"><svg width="40" height="40" viewBox="0 0 40 40" fill="none" stroke="#fff" stroke-width="2"><circle cx="20" cy="20" r="12"/><path d="M20 8v12h12"/></svg></div>
      <h4>ASSET MANAGEMENT</h4>
      <p>Sed ut perspiciatis unde omnis iste natus error sit voluptatem accusanti doloremque laudantium, totam rem aperiam</p>
      <a>LEARN MORE</a>
    </article>
    <article class="card">
      <div class="card-photo" role="img" aria-label="Stacks of coins with a glowing market line" style="background:linear-gradient(135deg,#2c3a52,#c08a3e 60%,#3b4660)"></div>
      <div class="card-icon"><svg width="40" height="40" viewBox="0 0 40 40" fill="none" stroke="#fff" stroke-width="2"><path d="M8 32h24M12 28V18M20 28V12M28 28V20"/><circle cx="28" cy="12" r="4"/></svg></div>
      <h4>PORTFOLIO OPTIMIZATION</h4>
      <p>Sed ut perspiciatis unde omnis iste natus error sit voluptatem accusanti doloremque laudantium, totam rem aperiam</p>
      <a>LEARN MORE</a>
    </article>
  </div>
</section>

<section class="abs faq">
  <h2 class="abs heading">FREQUENTLY ASKED QUESTIONS<span class="underline"></span></h2>
  <div class="abs faq-list">
    <div class="faq-item">What is a registered investment advisor? Are you a registered investment advisor?<span class="faq-plus"><svg width="26" height="26" viewBox="0 0 26 26" stroke="#fff" stroke-width="2"><path d="M13 2v22M2 13h22"/></svg></span></div>
    <div class="faq-item">What does being an independent financial advisor mean? Why does it matter?<span class="faq-plus"><svg width="26" height="26" viewBox="0 0 26 26" stroke="#fff" stroke-width="2"><path d="M13 2v22M2 13h22"/></svg></span></div>
    <div class="faq-item">What is a fiduciary? Are you a fiduciary?<span class="faq-plus"><svg width="26" height="26" viewBox="0 0 26 26" stroke="#fff" stroke-width="2"><path d="M13 2v22M2 13h22"/></svg></span></div>
    <div class="faq-item">What is a fiduciary? Are you a fiduciary?<span class="faq-plus"><svg width="26" height="26" viewBox="0 0 26 26" stroke="#fff" stroke-width="2"><path d="M13 2v22M2 13h22"/></svg></span></div>
    <div class="faq-item">What is a custodian? Are you a custodian?<span class="faq-plus"><svg width="26" height="26" viewBox="0 0 26 26" stroke="#fff" stroke-width="2"><path d="M13 2v22M2 13h22"/></svg></span></div>
    <div class="faq-item">What are your fees? How much will I pay?<span class="faq-plus"><svg width="26" height="26" viewBox="0 0 26 26" stroke="#fff" stroke-width="2"><path d="M13 2v22M2 13h22"/></svg></span></div>
  </div>
</section>

<section class="abs contact" role="img" aria-label="Sunlit mountain range at dusk behind the contact area">
  <h2>GET IN TOUCH</h2>
  <p class="abs lead">At vero eos et accusamus et iustignissimos ducimus qui blanditiis praesentium voluptatum deleniti atque corrupti quos dolores</p>
  <div class="abs info">
    <h5>LOCATION:</h5><p>2810 Alder Ln, Suite #204<br>Brookmere, VA 22970</p>
    <h5>EMAIL ADDRESS:</h5><p>info@ravenholtwealth.example</p>
    <h5>CALL US NOW:</h5><p>(555) 014-2290</p>
    <h5>FOLLOW NOW:</h5>
    <div class="socials"><span></span><span></span><span></span><span></span></div>
  </div>
  <form class="abs form">
    <h5>DROP YOUR MESSAGE</h5>
    <div class="field">Jonathan Doe<svg width="20" height="20" viewBox="0 0 20 20" fill="none" stroke="#666" stroke-width="1.4"><circle cx="10" cy="7" r="4"/><path d="M3 18c1-4 4-6 7-6s6 2 7 6"/></svg></div>
    <div class="field">Email Address<svg width="20" height="20" viewBox="0 0 20 20" fill="none" stroke="#666" stroke-width="1.4"><rect x="2" y="5" width="16" height="11"/><path d="M2 5l8 6 8-6"/></svg></div>
    <div class="field tall">Message<svg width="22" height="20" viewBox="0 0 22 20" fill="none" stroke="#666" stroke-width="1.4"><path d="M3 9a8 6 0 1 1 4 5l-4 2 1-4z"/></svg></div>
    <div class="btn">CONTACT US NOW</div>
  </form>
</section>

<footer class="abs footer">
  <div class="brand"><span class="brand-mark"></span>RAVENHOLT WEALTH</div>
  <div class="socials"><span></span><span></span><span></span><span></span></div>
  <span class="vrule" style="left:399px"></span>
  <span class="vrule" style="left:611px"></span>
  <span class="vrule" style="left:823px"></span>
  <div class="fcol" style="left:465px"><h6>Quick Link</h6><ul><li>Home</li><li>About</li><li>FAQs</li><li>Services</li><li>Contact</li></ul></div>
  <div class="fcol" style="left:677px"><h6>Other Link</h6><ul><li>Who We Are</li><li>Career</li><li>News</li><li>Resources</li><li>Contact</li></ul></div>
  <div class="fcol" style="left:892px"><h6>Contact Info</h6>
    <div class="row"><svg width="12" height="16" viewBox="0 0 12 16" fill="#fff"><path d="M6 0a6 6 0 0 1 6 6c0 4-6 10-6 10S0 10 0 6a6 6 0 0 1 6-6zm0 3.5a2.5 2.5 0 1 0 0 5 2.5 2.5 0 0 0 0-5z"/></svg><span>2810 Alder Ln, Suite #204<br>Brookmere, VA 22970</span></div>
    <div class="row"><svg width="14" height="14" viewBox="0 0 14 14" fill="none" stroke="#fff" stroke-width="1.5"><path d="M3 1l2 3-1.5 1.5a8 8 0 0 0 5 5L10 9l3 2-1 2.5C6 13 1 8 .5 2z"/></svg><span>(555) 014-2290</span></div>
    <div class="row"><svg width="14" height="12" viewBox="0 0 14 12" fill="#fff"><path d="M0 1h14v10H0zM0 1l7 5 7-5" stroke="#0b63b8"/></svg><span>info@ravenholtwealth.example</span></div>
  </div>
  <div class="copyright">Copyright © 2022 -&nbsp; Ravenholt Wealth. All Right Reserved</div>
  <div class="legal">Privacy Policy&nbsp; |&nbsp; Terms &amp; Conditions</div>
</footer>

</body>
</html>
```